Exhibition stand - Create vector files from word document plans for printing

See attached documents. I need all six word doc plans to be created into PDF/EPS (no bleed) that can be printed. They are for a shell scheme exhibition stand. Each panel is 923 x 2340mm (width x height) but need to be supplied to the printer at 25% size.
Hex colours #1c7c8c and #5b5b5c
Please align images etc, so that its symmetrical. Font is Arthaus.
The silhouettes are simply decoration, so please mix and match. Please feel free to add some touches if you think its appropriate.

```html
<!DOCTYPE html>
<html lang="en">
<head>
<meta charset="utf-8">
<title>Brightleaf Therapy – exhibition stand panels</title>
<link href="https://fonts.googleapis.com/css2?family=Comfortaa:wght@700&family=Roboto:wght@400&display=swap" rel="stylesheet">
<style>
  :root{
    --teal:#1c7c8c;
    --grey:#5b5b5c;
    --white:#ffffff;
    --page:#ffffff;
    --edge:#9a9a9a;
    --figure-light:#f2f2f2;
    --figure-mid:#c4c4c5;
  }
  *{box-sizing:border-box;margin:0;padding:0}
  html,body{width:1200px;height:500px;overflow:hidden;background:var(--page)}
  .stand{position:relative;width:1200px;height:500px;border:1px solid var(--edge)}
  .panel{position:absolute;top:22px;width:180px;height:458px;overflow:hidden}
  .panel--teal{background:var(--teal)}
  .panel--white{background:var(--white);border:1px solid #d4d4d4}
  .p1{left:20px}.p2{left:219px}.p3{left:417px}.p4{left:614px}.p5{left:810px}.p6{left:1003px}

  .top-strip{position:absolute;left:0;top:0;width:100%;height:13px;background:var(--teal)}

  /* logo */
  .logo-box{position:absolute;left:20px;top:30px;width:140px;height:64px;background:var(--white);border-radius:12px;
    display:flex;flex-direction:column;align-items:center;justify-content:center}
  .logo-name{font-family:'Comfortaa',sans-serif;font-weight:700;color:var(--teal);line-height:1;text-align:center}
  .logo-box .logo-name--main{font-size:17px;letter-spacing:.5px}
  .logo-box .logo-name--sub{font-size:10px;letter-spacing:1.5px;margin-top:5px}
  .logo-plain{position:absolute;left:10px;top:32px;width:160px;text-align:center}
  .logo-plain .logo-name--main{font-size:22px;letter-spacing:.5px}
  .logo-plain .logo-name--sub{font-size:12px;letter-spacing:2px;margin-top:7px}

  /* photos */
  .photo{position:absolute;border:3px solid var(--white)}
  .photo--right{border-left:none;border-radius:0 16px 16px 0}
  .photo--left{border-right:none;border-radius:16px 0 0 16px}
  .photo-frame{position:absolute;border:1.5px solid var(--white)}
  .photo-frame--right{border-left:none;border-radius:0 20px 20px 0}
  .photo-frame--left{border-right:none;border-radius:20px 0 0 20px}
  .photo-backer{position:absolute;background:var(--teal)}

  /* silhouette band */
  .figures-band{position:absolute;left:0;top:332px;width:100%;height:88px;background:var(--white)}
  .figures-band::before,.figures-band::after{content:"";position:absolute;left:0;width:100%;height:3px;background:var(--teal);z-index:1}
  .figures-band::before{top:2px}
  .figures-band::after{bottom:2px}
  .figures{position:absolute;left:0;right:0;top:8px;bottom:8px;
    background:linear-gradient(180deg,var(--white) 0%,var(--figure-light) 35%,var(--figure-mid) 100%)}

  /* contact */
  .contact{position:absolute;left:11px;top:399px;width:160px;height:60px;background:var(--teal);border-radius:12px 12px 0 0;
    padding:14px 0 0 12px}
  .contact-line{display:flex;align-items:center;gap:5px;font-family:'Roboto',sans-serif;font-size:9.3px;color:var(--white);height:19px;white-space:nowrap}
  .contact-line svg{flex:none}

  /* services */
  .title-frame{position:absolute;left:-4px;top:34px;width:158px;height:120px;border:1.5px solid var(--teal);border-left:none;border-radius:0 14px 14px 0}
  .title-box{position:absolute;left:13px;top:45px;width:148px;height:97px;background:var(--teal);border-radius:12px;
    padding:12px 0 0 17px}
  .title{font-family:'Comfortaa',sans-serif;font-weight:700;color:var(--white);font-size:19px;line-height:25px;white-space:nowrap}
  .services-wrap{position:absolute;left:34px;top:183px;width:150px;height:200px}
  .services-cap{position:absolute;left:8px;width:142px;height:12px;background:var(--teal)}
  .services-cap--top{top:0;border-radius:10px 0 0 0}
  .services-cap--bottom{bottom:0;border-radius:0 0 0 10px}
  .services-card{position:absolute;left:0;top:8px;width:150px;height:184px;background:var(--white);
    border:1.5px solid var(--teal);border-right:none;border-radius:12px 0 0 12px;padding:16px 0 0 11px}
  .services-list{list-style:none}
  .services-list li{display:flex;align-items:center;gap:6px;font-family:'Comfortaa',sans-serif;font-weight:700;
    color:var(--teal);font-size:11.4px;height:19.2px;white-space:nowrap}
  .services-list li::before{content:"";width:4px;height:4px;border-radius:50%;background:var(--grey);flex:none}
  .social-bar{position:absolute;left:0;top:417px;width:161px;height:42px;background:var(--teal);border-radius:0 12px 0 0;
    display:flex;align-items:center;justify-content:space-around;padding:0 12px 6px 10px}
  .social-dot{width:17px;height:17px;border-radius:50%;background:var(--white)}

  .base{position:absolute;left:0;top:425px;width:100%;height:33px;background:var(--teal)}
</style>
</head>
<body>
<main class="stand">

  <section class="panel panel--teal p1">
    <div class="logo-box">
      <span class="logo-name logo-name--main">BRIGHTLEAF</span>
      <span class="logo-name logo-name--sub">THERAPY</span>
    </div>
    <div class="photo-frame photo-frame--right" style="left:0;top:126px;width:167px;height:164px"></div>
    <div class="photo photo--right" role="img" aria-label="Photo: wheelchair user fishing from a wooden jetty on a lake under a blue sky"
      style="left:0;top:129px;width:164px;height:158px;background:linear-gradient(180deg,#8fb4dc 0%,#c9dcee 40%,#3c5d8a 62%,#2f4e78 80%,#b08a5e 100%)"></div>
    <div class="figures-band"><div class="figures" role="img" aria-label="Grey silhouettes of wheelchair users with family"></div></div>
    <div class="base"></div>
  </section>

  <section class="panel panel--teal p2">
    <div class="photo-frame photo-frame--right" style="left:0;top:31px;width:161px;height:121px"></div>
    <div class="photo photo--right" role="img" aria-label="Photo: two young women in wheelchairs chatting in a bright hallway"
      style="left:0;top:33px;width:154px;height:117px;background:linear-gradient(135deg,#c9b49a,#e7ddd0 45%,#8d8f86 75%,#5a6b57)"></div>
    <div class="photo-frame photo-frame--left" style="left:40px;top:180px;width:140px;height:125px"></div>
    <div class="photo photo--left" role="img" aria-label="Photo: man in a wheelchair in an autumn park with golden trees"
      style="left:47px;top:184px;width:133px;height:118px;background:linear-gradient(160deg,#e2a72a,#f0c34a 45%,#b9822c 75%,#8d7a64)"></div>
    <div class="figures-band"><div class="figures" role="img" aria-label="Grey silhouettes of wheelchair users with a dog, a partner and a child with a balloon"></div></div>
    <div class="base"></div>
  </section>

  <section class="panel panel--white p3">
    <div class="top-strip"></div>
    <div class="logo-plain">
      <div class="logo-name logo-name--main">BRIGHTLEAF</div>
      <div class="logo-name logo-name--sub">THERAPY</div>
    </div>
    <div class="photo-backer" style="left:10px;top:108px;width:150px;height:118px;border-radius:0 14px 14px 0"></div>
    <div class="photo photo--right" role="img" aria-label="Photo: smiling man in a denim jacket using a wheelchair on a park path"
      style="left:0;top:104px;width:154px;height:120px;border-width:2px;background:linear-gradient(170deg,#b9c7a4,#8fb25a 45%,#5f8a38 65%,#9a9a94)"></div>
    <div class="photo-backer" style="left:20px;top:260px;width:150px;height:113px;border-radius:14px 0 0 14px"></div>
    <div class="photo photo--left" role="img" aria-label="Photo: therapist stretching the leg of an older patient lying on a treatment table"
      style="left:28px;top:255px;width:152px;height:116px;border-width:2px;background:linear-gradient(135deg,#f1f2f3,#dfe3e6 40%,#8a8d95 70%,#d8c9a8)"></div>
    <div class="contact">
      <div class="contact-line">
        <svg width="10" height="10" viewBox="0 0 10 10"><rect x="1" y="2" width="8" height="6" fill="none" stroke="#fff" stroke-width="1"/><path d="M1 2l4 3 4-3" fill="none" stroke="#fff" stroke-width="1"/></svg>
        <span>info@brightleaftherapy.co.uk</span>
      </div>
      <div class="contact-line">
        <svg width="10" height="10" viewBox="0 0 10 10"><circle cx="5" cy="5" r="4" fill="none" stroke="#fff" stroke-width="1"/><path d="M1 5h8M5 1c-2 2.5-2 5.5 0 8M5 1c2 2.5 2 5.5 0 8" fill="none" stroke="#fff" stroke-width=".8"/></svg>
        <span>brightleaftherapy.co.uk</span>
      </div>
    </div>
  </section>

  <section class="panel panel--white p4">
    <div class="top-strip"></div>
    <div class="title-frame"></div>
    <div class="title-box">
      <h1 class="title">private<br>wheelkshair<br>services</h1>
    </div>
    <div class="services-wrap">
      <div class="services-cap services-cap--top"></div>
      <div class="services-cap services-cap--bottom"></div>
      <div class="services-card">
        <ul class="services-list">
          <li>assessment</li>
          <li>product Trial</li>
          <li>prescription</li>
          <li>reports</li>
          <li>procurement</li>
          <li>review</li>
          <li>skill Training</li>
          <li>expert Wintessess</li>
        </ul>
      </div>
    </div>
    <div class="social-bar">
      <span class="social-dot"></span><span class="social-dot"></span><span class="social-dot"></span><span class="social-dot"></span>
    </div>
  </section>

  <section class="panel panel--teal p5">
    <div class="photo-frame photo-frame--right" style="left:0;top:13px;width:165px;height:141px"></div>
    <div class="photo photo--right" role="img" aria-label="Photo: young man in an all-terrain wheelchair on a grassy country track"
      style="left:0;top:16px;width:158px;height:135px;background:linear-gradient(150deg,#4f7a2c,#7fa446 40%,#9a8a6c 70%,#5d6d3a)"></div>
    <div class="photo-frame photo-frame--left" style="left:18px;top:175px;width:162px;height:139px"></div>
    <div class="photo photo--left" role="img" aria-label="Photo: older man riding a hand-cycle attachment on a wheelchair beside a hedge"
      style="left:26px;top:179px;width:154px;height:132px;background:linear-gradient(160deg,#3e6a2a,#6d9447 45%,#9a9b98 75%,#7b7c7c)"></div>
    <div class="figures-band"><div class="figures" role="img" aria-label="Grey silhouettes of wheelchair users with a dog, a partner and a child with a balloon"></div></div>
    <div class="base"></div>
  </section>

  <section class="panel panel--teal p6">
    <div class="logo-box">
      <span class="logo-name logo-name--main">BRIGHTLEAF</span>
      <span class="logo-name logo-name--sub">THERAPY</span>
    </div>
    <div class="photo-frame photo-frame--left" style="left:24px;top:126px;width:156px;height:164px"></div>
    <div class="photo photo--left" role="img" aria-label="Photo: close-up of a hand on a wheelchair push rim"
      style="left:31px;top:129px;width:149px;height:158px;background:linear-gradient(135deg,#d9d5cf,#bdb8b0 40%,#3a4a6e 70%,#5a4c3e)"></div>
    <div class="figures-band"><div class="figures" role="img" aria-label="Grey silhouettes of wheelchair users with family"></div></div>
    <div class="base"></div>
  </section>

</main>
</body>
</html>
```